Business Card Design

I would like a new business card design for an accounting firm that specializes in resolving clients tax problems. I want the card to give the impression that we are not your typical stodgy accounting firm, but at the same time we will get the job done.
Industry/Entity Type
Business
Contact Information for Business Card
Dorian T Welsby
Certified Public Accountant
38-27 52nd Street
Brackenfield, NV 11287
Tel: (718) 555-0142
Fax: (888) 555-0199
e-mail: dtwthecpa@ledgerpost.com
website: harborfilingreliefexperts.com

```html
<!DOCTYPE html>
<html lang="en">
<head>
<meta charset="utf-8">
<title>Dorian T Welsby — Business Card</title>
<link rel="stylesheet" href="https://fonts.googleapis.com/css2?family=Roboto:wght@400;500;700&display=swap">
<style>
  :root {
    --backdrop: #e8e4df;
    --sky-blue: #0a7cc4;
    --navy: #213a66;
    --ink: #000000;
    --paper: #ffffff;
  }
  html, body {
    margin: 0;
    padding: 0;
    width: 1200px;
    height: 800px;
    overflow: hidden;
    background: var(--backdrop);
    font-family: "Roboto", Arial, sans-serif;
  }
  .stage {
    position: relative;
    width: 1200px;
    height: 800px;
  }
  .business-card {
    position: absolute;
    left: 150px;
    top: 150px;
    width: 592px;
    height: 328px;
    transform: scale(1.52);
    transform-origin: 0 0;
    overflow: hidden;
    box-shadow: 0 3px 10px rgba(0,0,0,0.18);
    color: var(--paper);
  }
  .card-shapes {
    position: absolute;
    inset: 0;
    width: 592px;
    height: 328px;
  }
  .shape-top { fill: var(--sky-blue); }
  .shape-bottom { fill: var(--navy); }
  .shape-wedge { fill: var(--ink); }

  .identity {
    position: absolute;
    left: 304px;
    top: 51px;
  }
  .person-name {
    margin: 0;
    font-size: 27px;
    font-weight: 700;
    letter-spacing: 1.4px;
    line-height: 1;
    text-transform: uppercase;
  }
  .person-title {
    margin: 8px 0 0;
    font-size: 15px;
    font-weight: 400;
    letter-spacing: 0.45px;
    text-transform: uppercase;
  }

  .contact-row {
    position: absolute;
    left: 306px;
    display: flex;
    align-items: flex-start;
    gap: 9px;
    font-size: 14.5px;
    line-height: 19px;
    letter-spacing: 0.5px;
  }
  .contact-row .icon {
    width: 20px;
    height: 19px;
    flex: none;
  }
  .contact-row p { margin: 0; }
  .row-phone   { top: 110px; letter-spacing: 1px; }
  .row-email   { top: 180px; }
  .row-web     { top: 208px; }
  .row-address { top: 235px; }
  .icon-fill { fill: var(--paper); }
  .icon-line { fill: none; stroke: var(--paper); stroke-width: 1.4; }
</style>
</head>
<body>
<main class="stage">
  <article class="business-card">
    <svg class="card-shapes" viewBox="0 0 592 328" aria-hidden="true">
      <rect class="shape-top" x="0" y="0" width="592" height="164"/>
      <rect class="shape-bottom" x="0" y="164" width="592" height="164"/>
      <path class="shape-wedge" d="M0 0 L22 0 Q175 70 300 164 Q175 258 22 328 L0 328 Z"/>
    </svg>

    <header class="identity">
      <h1 class="person-name">Dorian T Welsby</h1>
      <p class="person-title">Certified Public Accountant</p>
    </header>

    <div class="contact-row row-phone">
      <svg class="icon" viewBox="0 0 20 19" aria-hidden="true">
        <path class="icon-fill" d="M4.2 1.5c.6-.4 1.3-.2 1.7.4l1.7 2.7c.3.6.2 1.2-.3 1.6l-1.2 1c.9 1.9 2.4 3.5 4.3 4.5l1-1.2c.4-.5 1.1-.6 1.6-.3l2.7 1.6c.6.4.8 1.1.4 1.7l-1 1.7c-.5.8-1.5 1.2-2.4.9C7.1 15.2 3.4 11.4 2 5.6c-.2-.9.1-1.8.9-2.3z"/>
      </svg>
      <p>Tel: (718) 555-0142<br>Fax: (888) 555-0199</p>
    </div>

    <div class="contact-row row-email">
      <svg class="icon" viewBox="0 0 20 19" aria-hidden="true">
        <rect class="icon-line" x="1.5" y="4" width="17" height="11"/>
        <path class="icon-line" d="M1.5 4 L10 10.5 L18.5 4"/>
      </svg>
      <p>dtwthecpa@ledgerpost.com</p>
    </div>

    <div class="contact-row row-web">
      <svg class="icon" viewBox="0 0 20 19" aria-hidden="true">
        <circle class="icon-line" cx="10" cy="9.5" r="8"/>
        <ellipse class="icon-line" cx="10" cy="9.5" rx="3.5" ry="8"/>
        <path class="icon-line" d="M2 9.5 H18 M3.2 5.5 H16.8 M3.2 13.5 H16.8"/>
      </svg>
      <p>harborfilingreliefexperts.com</p>
    </div>

    <div class="contact-row row-address">
      <svg class="icon" viewBox="0 0 20 19" aria-hidden="true">
        <path class="icon-fill" d="M10 1.5c-3 0-5.3 2.3-5.3 5.2 0 3.8 5.3 10.3 5.3 10.3s5.3-6.5 5.3-10.3c0-2.9-2.3-5.2-5.3-5.2zm0 7.3a2 2 0 1 1 0-4 2 2 0 0 1 0 4z"/>
      </svg>
      <p>38-27 52nd Street<br>Brackenfield, NV 11287</p>
    </div>
  </article>
</main>
</body>
</html>
```